Business Card Design Project For Moving Company

Hello,

We need the business card to be 2 sided and we were thinking to use the logo on the front of the card (see file 1 attached) and the text "logo" (see file 2 attached) in the back of the card. We're looking for a powerful design that will help us build our brand, as our company is new.
We are a full service moving company (no storage) located in San Diego, CA, USA. The design should communicate to our potential customers that we have the highest level of service, customer satisfaction is our number one goal, our team is professional and efficient.

Thank you,

Gil
Updates

Project Deadline Extended
Reason: We would like to have more time to provide feedback for the designs already submitted. Thank you, Gil

Industry/Entity Type

Moving Company

Requirements
Must have
• Front of the card must have the following text and logo:
Haul Brightway, Inc
Residential And Commercial
Local And Long Distance
Address: 3917 Alder Crest Rd, #412,
San Diego, CA, 92087
P: 855-372-LIFT (5438)
F: 858-291-4476
info@haul-brightway.com
www.haul-brightway.com

Back of the card must have the following text and text "logo" (file 2 attached):

The best compliment we can ever receive is a referral from our clients.

```html
<!DOCTYPE html>
<html lang="en">
<head>
<meta charset="utf-8">
<title>Haul Brightway – Business Card</title>
<link href="https://fonts.googleapis.com/css2?family=Arimo:ital,wght@0,400;0,700;1,400&display=swap" rel="stylesheet">
<style>
  :root {
    --navy: #14244a;
    --red: #d8261c;
    --white: #ffffff;
    --backdrop: #e9eaec;
  }
  * { margin: 0; padding: 0; box-sizing: border-box; }
  html, body {
    width: 1200px;
    height: 893px;
    overflow: hidden;
    background: var(--backdrop);
    font-family: "Arimo", Arial, sans-serif;
  }
  .canvas {
    position: relative;
    width: 1200px;
    height: 893px;
  }
  .card {
    position: absolute;
    left: 280px;
    width: 640px;
    height: 366px;
    background: var(--navy);
    overflow: hidden;
    color: var(--white);
  }
  .card--back { top: 60px; }
  .card--front { top: 467px; }

  /* Back side */
  .back-band {
    position: absolute;
    left: 0;
    bottom: 0;
    width: 100%;
    height: 100%;
  }
  .back-brand {
    position: absolute;
    top: 110px;
    left: 0;
    width: 100%;
    display: flex;
    justify-content: center;
    align-items: center;
    gap: 12px;
  }
  .brand-square {
    width: 30px;
    height: 30px;
    background: var(--red);
  }
  .brand-name {
    font-weight: 700;
    color: var(--red);
    font-size: 36px;
    letter-spacing: 0.5px;
    text-transform: uppercase;
  }
  .back-quote {
    position: absolute;
    top: 196px;
    left: 60px;
    right: 60px;
    text-align: center;
    font-style: italic;
    font-size: 17px;
    line-height: 1.4;
  }

  /* Front side */
  .front-band {
    position: absolute;
    left: 0;
    bottom: 0;
    width: 100%;
    height: 18px;
    background: var(--red);
  }
  .front-circle {
    position: absolute;
    right: 36px;
    top: 60px;
    width: 210px;
    height: 210px;
    border-radius: 50%;
    background: var(--red);
  }
  .front-name {
    position: absolute;
    top: 28px;
    left: 36px;
    font-weight: 700;
    font-size: 40px;
    color: var(--white);
    text-transform: uppercase;
    letter-spacing: 0.5px;
  }
  .services {
    position: absolute;
    top: 86px;
    left: 36px;
    width: 310px;
    text-align: center;
    font-weight: 700;
    font-size: 18px;
    line-height: 1.2;
    list-style: none;
  }
  .contact {
    position: absolute;
    top: 204px;
    left: 36px;
    font-weight: 700;
    font-size: 13px;
    line-height: 1.35;
    font-style: normal;
  }
  .contact .web { margin-top: 14px; }
</style>
</head>
<body>
<main class="canvas">

  <section class="card card--back" aria-label="Back of card">
    <svg class="back-band" viewBox="0 0 640 366" aria-hidden="true">
      <polygon points="0,288 640,340 640,366 0,366" fill="var(--red)"/>
      <polygon points="0,300 640,352 640,366 0,366" fill="var(--navy)"/>
    </svg>
    <div class="back-brand">
      <span class="brand-square" aria-hidden="true"></span>
      <span class="brand-name">Haul Brightway</span>
    </div>
    <p class="back-quote">“The best compliment we can ever receive is a referral from our clients.”</p>
  </section>

  <section class="card card--front" aria-label="Front of card">
    <span class="front-circle" aria-hidden="true"></span>
    <h1 class="front-name">Haul Brightway</h1>
    <ul class="services">
      <li>Moving ◆ Packing ◆ Loading</li>
      <li>Residential ◆ Commercial</li>
      <li>Local ◆ Long Distance</li>
    </ul>
    <address class="contact">
      <div>3917 Alder Crest Rd, #412,</div>
      <div>San Diego, CA, 92087</div>
      <div>P: 855-372-LIFT (5438)</div>
      <div>F: 858-291-4476</div>
      <div class="web">info@haul-brightway.com</div>
      <div>www.haul-brightway.com</div>
    </address>
    <span class="front-band" aria-hidden="true"></span>
  </section>

</main>
</body>
</html>
```